Brill's Jewelers website (www.brillsjewelers-example.com)

We are in need of a web storefront for a retail Jewelry store.
www.brillsjewelers-example.com
https://www.facebook.com/Brills-Jewelers-Palm-Vista-740315928461257/

Brill's Jewelers is located in Coral Gables, Florida. The store has been family owned and operated since 1958. Their focus customers are high-income families that care about quality over the brand name. They mostly sell fashion jewelry and diamonds up to 8 carats. We are looking for a simple minimalistic site that their customers can view their inventory and purchase items online.

Competitors websites:
https://www.orvinjewelers-example.com/
http://www.pelvaro-example.com/
http://truecutjewelers-example.com/

Pages:
-Home (with message bulletin)
-Jewelry
We would be able to create the subpages ie Rings, Bracelets, Earrings, Necklaces, Estate, Watches, Men's, Children's
-Services
We would need sub pages ie Appraisals, Consignment, Repairs
-About us
-Contact

Target Market(s)

Local wealthy families

Coding

Number of Pages Required

Font styles to use
Serif

Requirements
Must have
• -An E-commerce site customers can buy jewelry online.
-An easy process internally to add new items to the site
-Colors are Black and White or Black and Gold
Nice to have
• I would like to stay away from face shots of random models in stock photos. I want the jewelry pieces as the focus, not models.

```html
<!DOCTYPE html>
<html lang="en">
<head>
<meta charset="utf-8">
<title>Brill's Jewelers – Desktop and Mobile Home</title>
<link rel="stylesheet" href="https://fonts.googleapis.com/css2?family=Roboto:wght@400;500;700;900&family=Open+Sans:wght@400&display=swap">
<style>
:root{
  --board:#e8e8e8;
  --black:#000;
  --ink:#0b0c11;
  --white:#fff;
  --text-dark:#111;
  --muted:#cfcfcf;
  --cookie:#3a3a3a;
  --label:#333;
}
*{margin:0;padding:0;box-sizing:border-box}
html,body{width:1200px;height:1200px;overflow:hidden}
body{background:var(--board);font-family:"Roboto",Arial,sans-serif;position:relative;color:var(--white)}
.board-label{position:absolute;top:38px;font-family:"Open Sans",Arial,sans-serif;font-size:20px;color:var(--label)}
.artboard{position:absolute;top:70px;height:1060px;background:var(--black);overflow:hidden;box-shadow:0 2px 10px rgba(0,0,0,.12)}
.desktop{left:244px;width:528px}
.mobile{left:810px;width:145px}
.abs{position:absolute;white-space:nowrap}
.brand{font-weight:900;letter-spacing:1px;color:var(--white);text-align:center}
.tagline{font-size:4.5px;letter-spacing:.6px;color:var(--muted);text-align:center}
.nav-item{font-size:6.5px;font-weight:500;letter-spacing:.2px}
.icons{display:flex;gap:4px;align-items:center}
.icons span{font-size:4px}
.hero-bg{position:absolute;left:0;top:28px;width:528px;height:294px;background:linear-gradient(180deg,#0a0a0d 0%,var(--ink) 100%)}
.photo{position:absolute;z-index:0}
.hero-title{font-weight:900;font-size:18.5px;line-height:29px;z-index:2}
.hero-copy{font-size:7px;line-height:11.5px;white-space:normal;color:#e6e6e6;z-index:2}
.cta{font-size:10px;font-weight:500;z-index:2}
.section-white{position:absolute;left:0;width:528px;background:var(--white);color:var(--text-dark)}
.section-title{font-weight:900;font-size:19px}
.cat-link{font-size:11.5px;color:var(--text-dark)}
.block-label{font-size:10px;font-weight:500}
.foot-head{font-size:5.5px;font-weight:500;padding-bottom:2px;border-bottom:.7px solid #bbb}
.foot-item{font-size:5px;font-weight:500;letter-spacing:.1px}
.cookie-bar{position:absolute;left:0;top:1033px;width:528px;height:27px;background:var(--cookie)}
.cookie-text{font-size:4px;line-height:6px;white-space:normal;width:370px;color:#e9e9e9}
.cookie-btn{background:var(--black);font-size:4.5px;padding:4px 6px}
.m-title{font-weight:900;font-size:9.5px;line-height:15px;text-align:center;width:145px;left:0}
.m-copy{font-size:5.3px;line-height:9.6px;text-align:center;white-space:normal;width:104px;left:20px;color:#e6e6e6}
.center{left:0;width:100%;text-align:center}
</style>
</head>
<body>

<div class="board-label" style="left:244px">Desktop</div>
<div class="board-label" style="left:812px">Mobile</div>

<!-- Desktop home page -->
<main class="artboard desktop">
  <div class="hero-bg"></div>
  <div class="photo" role="img" aria-label="Two brilliant cut diamonds on a black reflective surface" style="left:245px;top:130px;width:283px;height:175px;background:radial-gradient(ellipse at 36% 40%,#8e8f96 0%,#2a2b31 20%,transparent 36%),radial-gradient(ellipse at 74% 40%,#a4a5ac 0%,#34353b 22%,transparent 38%),#07080b"></div>

  <div class="abs brand" style="left:0;width:528px;top:14px;font-size:15px">BRILL'S</div>
  <div class="abs tagline" style="left:0;width:528px;top:34px">YOUR HOMETOWN JEWELER</div>

  <div class="abs icons" style="left:456px;top:18px">
    <svg width="7" height="8" viewBox="0 0 7 8" fill="none" stroke="#fff" stroke-width=".9"><circle cx="3.5" cy="2.3" r="1.7"/><path d="M.6 7.6c0-1.8 1.3-3 2.9-3s2.9 1.2 2.9 3z"/></svg>
    <svg width="9" height="8" viewBox="0 0 9 8" fill="none" stroke="#fff" stroke-width=".9"><path d="M4.5 7.3 1.1 4A2 2 0 0 1 4.5 1.4 2 2 0 0 1 7.9 4z"/></svg><span>0</span>
    <svg width="8" height="8" viewBox="0 0 8 8" fill="none" stroke="#fff" stroke-width=".9"><path d="M.3 .8h1.3l1 4.4h4.1l.9-3.2H2"/><circle cx="3" cy="6.9" r=".6"/><circle cx="6" cy="6.9" r=".6"/></svg><span>0</span>
  </div>

  <nav>
    <div class="abs nav-item" style="left:106px;top:55px">HOME</div>
    <div class="abs nav-item" style="left:171px;top:55px">JEWELRY</div>
    <div class="abs nav-item" style="left:246px;top:55px">SERVICES</div>
    <div class="abs nav-item" style="left:323px;top:55px">ABOUT</div>
    <div class="abs nav-item" style="left:391px;top:55px">CONTACT</div>
  </nav>

  <div class="abs hero-title" style="left:57px;top:129px">Your Hometown Jeweler<br>Just Got a New Home</div>
  <p class="abs hero-copy" style="left:59px;top:195px;width:180px">You have trusted us for decades with your fine jewelry, custom designs, and repairs. Now come in and see what's in store!</p>
  <div class="abs cta" style="left:59px;top:255px">Visit&nbsp; us today&nbsp; »</div>

  <div class="abs" style="left:0;top:312px;width:148px;height:104px;background:var(--black)"></div>
  <div class="abs block-label" style="left:57px;top:322px">NEW ARRIVALS</div>
  <div class="photo" role="img" aria-label="Gold and diamond stacked bracelets" style="left:148px;top:322px;width:94px;height:94px;background:linear-gradient(135deg,#f4efe6,#c8a052 55%,#e9dcc0)"></div>
  <div class="photo" role="img" aria-label="Cushion halo diamond engagement ring" style="left:243px;top:322px;width:94px;height:94px;background:radial-gradient(circle at 50% 50%,#cfd4da,#f6f6f6 60%)"></div>
  <div class="photo" role="img" aria-label="Diamond flower drop earrings" style="left:338px;top:322px;width:94px;height:94px;background:linear-gradient(180deg,#fafafa,#e6e6e8)"></div>
  <div class="photo" role="img" aria-label="Rose gold diamond cuff bracelets" style="left:433px;top:322px;width:95px;height:94px;background:linear-gradient(135deg,#fbf3ee,#d99a78 55%,#f1d2bf)"></div>

  <section class="section-white" style="top:416px;height:96px">
    <div class="abs section-title" style="left:57px;top:37px">Our Jewelry</div>
    <div class="abs cat-link" style="left:226px;top:30px">Rings</div>
    <div class="abs cat-link" style="left:287px;top:30px">Bracelets</div>
    <div class="abs cat-link" style="left:363px;top:30px">Estate</div>
    <div class="abs cat-link" style="left:428px;top:30px">Men's</div>
    <div class="abs cat-link" style="left:226px;top:53px">Earrings</div>
    <div class="abs cat-link" style="left:287px;top:53px">Necklaces</div>
    <div class="abs cat-link" style="left:363px;top:53px">Watches</div>
    <div class="abs cat-link" style="left:428px;top:53px">Children's</div>
  </section>

  <section class="section-white" style="top:512px;height:213px">
    <div class="abs" style="left:0;top:0;width:148px;height:213px;background:var(--black)"></div>
    <div class="abs block-label" style="left:57px;top:20px;color:var(--white)">FEATURED</div>
    <div class="abs" style="left:182px;top:26px;font-size:12px;font-weight:500">Lumière Atelier</div>
    <div class="abs" style="left:192px;top:52px;font-size:8px">Petal Wings</div>
    <div class="photo" role="img" aria-label="Colourful enamel butterfly bangles, earrings, pendants and ring" style="left:180px;top:70px;width:320px;height:135px;background:radial-gradient(ellipse at 30% 60%,#e8b5c8 0%,#9ac6e6 25%,transparent 45%),radial-gradient(ellipse at 80% 40%,#f2d27a 0%,#e47a8a 20%,transparent 40%),#fff"></div>
  </section>

  <section class="section-white" style="top:725px;height:95px">
    <div class="abs section-title" style="left:57px;top:38px">Our Services</div>
    <div class="abs cat-link" style="left:226px;top:42px">Appraisals</div>
    <div class="abs cat-link" style="left:320px;top:42px">Consignment</div>
    <div class="abs cat-link" style="left:428px;top:42px">Repairs</div>
  </section>

  <footer>
    <div class="abs brand" style="left:61px;top:864px;font-size:12px;text-align:left">BRILL'S</div>
    <div class="abs tagline" style="left:61px;top:882px;text-align:left;font-size:4px">YOUR HOMETOWN JEWELER</div>

    <div class="abs foot-head" style="left:161px;top:873px">LINK&nbsp;&nbsp;&nbsp;&nbsp;&nbsp;&nbsp;&nbsp;&nbsp;</div>
    <div class="abs foot-item" style="left:161px;top:899px">JEWELRY</div>
    <div class="abs foot-item" style="left:161px;top:912px">SERVICES</div>
    <div class="abs foot-item" style="left:161px;top:925px">ABOUT</div>
    <div class="abs foot-item" style="left:161px;top:938px">CONTACT</div>

    <div class="abs foot-head" style="left:236px;top:873px">OPENING HOURS</div>
    <div class="abs foot-item" style="left:236px;top:899px">MON - FRI</div>
    <div class="abs foot-item" style="left:275px;top:899px">10 AM - 5:30 PM</div>
    <div class="abs foot-item" style="left:236px;top:912px">SATURDAY</div>
    <div class="abs foot-item" style="left:275px;top:912px">11 AM - 5:00 PM</div>

    <div class="abs foot-head" style="left:376px;top:873px">CONTACT</div>
    <div class="abs foot-item" style="left:376px;top:899px">TEL (555) 014 2290</div>
    <div class="abs foot-item" style="left:376px;top:913px">FAX (555) 014 2291</div>
    <div class="abs foot-item" style="left:375px;top:927px">HELLO@BRILLSJEWELERS-EXAMPLE.COM</div>
    <div class="abs foot-item" style="left:376px;top:941px;line-height:8px">88 HARBOR LANE, PALM<br>VISTA, FL 00000</div>

    <div class="abs foot-item" style="left:0;width:528px;text-align:center;top:999px;font-size:4.5px;font-weight:400">© Brill's Limited 2020. All Rights Reserved.</div>
  </footer>

  <div class="cookie-bar">
    <p class="abs cookie-text" style="left:35px;top:6px">BRILL'S uses cookies to improve your visit to this site and to offer services and messages suited to your interests. By continuing to browse our site, you agree to the use of these cookies. You can decline this use by clicking here</p>
    <div class="abs" style="left:416px;top:11px;font-size:4.5px;text-decoration:underline">Cookie Settings</div>
    <div class="abs cookie-btn" style="left:461px;top:7px">Accept All Cookies</div>
  </div>
</main>

<!-- Mobile home page -->
<main class="artboard mobile">
  <div class="abs icons" style="left:90px;top:10px">
    <svg width="7" height="8" viewBox="0 0 7 8" fill="none" stroke="#fff" stroke-width=".9"><circle cx="3.5" cy="2.3" r="1.7"/><path d="M.6 7.6c0-1.8 1.3-3 2.9-3s2.9 1.2 2.9 3z"/></svg>
    <svg width="9" height="8" viewBox="0 0 9 8" fill="none" stroke="#fff" stroke-width=".9"><path d="M4.5 7.3 1.1 4A2 2 0 0 1 4.5 1.4 2 2 0 0 1 7.9 4z"/></svg><span>0</span>
    <svg width="8" height="8" viewBox="0 0 8 8" fill="none" stroke="#fff" stroke-width=".9"><path d="M.3 .8h1.3l1 4.4h4.1l.9-3.2H2"/><circle cx="3" cy="6.9" r=".6"/><circle cx="6" cy="6.9" r=".6"/></svg><span>0</span>
  </div>
  <div class="abs brand" style="left:12px;top:27px;font-size:13px;text-align:left">BRILL'S</div>
  <div class="abs tagline" style="left:12px;top:45px;text-align:left;font-size:4px">YOUR HOMETOWN JEWELER</div>
  <svg class="abs" style="left:125px;top:36px" width="10" height="8" viewBox="0 0 10 8" stroke="#fff" stroke-width=".8"><path d="M0 1h10M0 4h10M0 7h10"/></svg>

  <div class="abs m-title" style="top:72px">Your Hometown Jeweler<br>Just Got a New Home</div>
  <p class="abs m-copy" style="top:107px">You have trusted us for decades with your fine jewelry, custom designs, and repairs. Now come in and see what's in store!</p>
  <div class="abs cta center" style="top:159px;font-size:9px">Visit&nbsp; us today&nbsp; »</div>
  <div class="photo" role="img" aria-label="Two brilliant cut diamonds on black" style="left:8px;top:177px;width:129px;height:86px;background:radial-gradient(ellipse at 32% 45%,#9a9ba2 0%,#2a2b31 24%,transparent 40%),radial-gradient(ellipse at 72% 45%,#a6a7ae 0%,#34353b 24%,transparent 40%),#0b0c10"></div>

  <div class="abs block-label center" style="top:311px;font-size:9.5px">NEW ARRIVALS</div>
  <div class="photo" role="img" aria-label="Gold and diamond stacked bracelets" style="left:25px;top:331px;width:95px;height:72px;background:linear-gradient(135deg,#f4efe6,#c8a052 55%,#e9dcc0)"></div>
  <div class="photo" role="img" aria-label="Cushion halo diamond engagement ring" style="left:25px;top:405px;width:95px;height:72px;background:radial-gradient(circle at 50% 50%,#cfd4da,#f6f6f6 60%)"></div>
  <div class="photo" role="img" aria-label="Diamond flower drop earrings" style="left:25px;top:479px;width:95px;height:72px;background:linear-gradient(180deg,#fafafa,#e6e6e8)"></div>
  <div class="photo" role="img" aria-label="Rose gold diamond cuff bracelets" style="left:25px;top:553px;width:95px;height:72px;background:linear-gradient(135deg,#fbf3ee,#d99a78 55%,#f1d2bf)"></div>

  <div class="abs block-label center" style="top:659px;font-size:9.5px">FEATURED</div>
  <div class="photo" role="img" aria-label="Colourful enamel butterfly jewelry collection" style="left:27px;top:680px;width:93px;height:75px;background:radial-gradient(ellipse at 35% 62%,#e8b5c8 0%,#9ac6e6 22%,transparent 42%),radial-gradient(ellipse at 78% 42%,#f2d27a 0%,#e47a8a 18%,transparent 36%),#fff"></div>

  <footer>
    <div class="abs brand center" style="top:783px;font-size:13px">BRILL'S</div>
    <div class="abs tagline center" style="top:802px;font-size:4px">YOUR HOMETOWN JEWELER</div>

    <div class="abs foot-head" style="left:27px;top:823px">LINK&nbsp;&nbsp;&nbsp;&nbsp;</div>
    <div class="abs foot-item" style="left:27px;top:841px">JEWELRY</div>
    <div class="abs foot-item" style="left:27px;top:854px">SERVICES</div>
    <div class="abs foot-item" style="left:27px;top:867px">ABOUT</div>

    <div class="abs foot-head" style="left:26px;top:896px">OPENING HOURS</div>
    <div class="abs foot-item" style="left:26px;top:914px">MON - FRI</div>
    <div class="abs foot-item" style="left:65px;top:917px">10 AM - 5:30 PM</div>
    <div class="abs foot-item" style="left:26px;top:927px">SATURDAY</div>
    <div class="abs foot-item" style="left:65px;top:927px">11 AM - 5:00 PM</div>

    <div class="abs foot-head" style="left:27px;top:955px">CONTACT</div>
    <div class="abs foot-item" style="left:27px;top:973px">TEL (555) 014 2290</div>
    <div class="abs foot-item" style="left:27px;top:987px">FAX (555) 014 2291</div>
    <div class="abs foot-item" style="left:25px;top:1001px;font-size:4.3px">HELLO@BRILLSJEWELERS-EXAMPLE.COM</div>
    <div class="abs foot-item" style="left:27px;top:1015px;line-height:8px">88 HARBOR LANE, PALM<br>VISTA, FL 00000</div>

    <div class="abs foot-item center" style="top:1049px;font-size:4px;font-weight:400">© Brill's Limited 2020. All Rights Reserved.</div>
  </footer>
</main>

</body>
</html>
```